依頼詳細
2016年に発足した一般吹奏楽団の3回目の演奏会となります。出演者の多くは10代、20代の若い世代が中心となり、音楽を通じて出会った仲間と共に日々活動を行なっています。男女問わず、若い世代からシニア世代まで、たくさんの方々に興味を持ってもらえるようなデザインを希望します。

チラシサイズはA4、チケットサイズは名刺サイズのもので作成お願いします。
チラシ表面には演奏会のイメージとなるものを、チラシ裏面はゲストの紹介及び団の紹介をお願いします。(両面カラー)
チケットはチラシ表面のイメージを使用したものでお願いします。(片面カラー)

【チラシ表面イメージ】
今回の演奏会では「七星の音色」をテーマにしております。
ユニバリアードイヤーにちなんで、七星=五つの大陸にちなんだ選曲をしました。
また、演奏会のメイン曲を交響曲第4番 「ウィンドウズ・オブ・ミナモト」にしました。東京ユニバリアードに開催にあたり、東京周辺の風景を描いた作品を元に作曲された曲を選曲しました。詳細は補足説明をご覧ください。

【チラシ裏面イメージ】
演奏会の一部で、ものまね芸人川端絵美里をゲストに迎え、コラボ企画を予定しております。全体の半分〜3分の2程を使用しゲストの紹介をできるようなものをお願いします。。ゲスト紹介は雑誌の表紙のようなデザインをイメージしております。
(※添付ファイルほか、インターネット上にある画像を使用して構わないとご本人から確認を取っています。)
全体の半分〜3分の1程を使用して当団の紹介。
当団の紹介文や写真を使用して作成をお願いします。

以下、ゲスト紹介の際にご使用ください。
ゲスト:川端 絵美里(ものまね芸人)
現役音楽教師のホンモノを超えたものまね芸
生年月日:11月3日
出身地:福島県
血液型:A型
身長:155cm
趣味:人間観察・映画鑑賞
特技:即興演奏(キーボード)
“ものまね界の帰国子女”鍛え上げられた歌声をご堪能下さい!
[主なネタ]
・即興で作曲(ピアノ弾き語り)
・QRZ36曲中に48人全員のモノマネ
・コラボシリーズ
〜prism×溝口沙耶〜
〜そよかぜびより×溝口沙耶〜
・アーティストから学ぶ音楽授業
…他多数

[主なレパートリー]
柏木美沙(本人公認) 風間千里 溝口沙耶 桐生ゆかり RENVA 水野麻衣 ノラ・ケストリッジ マリエル・ファブロ 古賀弥生 堀田真奈 西浦頼子 北野夏希 Pahama 宮下凛 瀬尾真琴 Tess K. FLARE 澪音 三雲紬 相沢律子 野村さつき VELT 石黒菜穂子 若松ことね ハル子・ブランデル 大槻みほ 森永朱里(きらめきサンフラワーX) 早瀬美智代 宇佐見玲奈 竹みね子 ルシア・ボレンテ ベロニカ・ミナ ポルテリアの世界 CMソングメドレー 羽鳥由紀メドレー 他多数
[主な出演]
ぺんぎんずのみんなでいっしょだよ(ひばりテレビ)クエスト☆芸能図鑑(KRN系)北条健太の水曜日のかがやく人へ(KRN系)ゴゴマルケ!(みなと放送)教えて!ベストテン(かもめテレビ)星組の振り分け☆(かもめテレビ)こだまのMEGAどっきりTV(KRN系)松井茂樹アワー 集まれみんなで!(ひばりテレビ)大笑いうりふたつ声まね東西歌対決スペシャル(ひばりテレビ)マンデーパレード『めざせ妖精王! 川端絵美里のコンビニ減量作戦』(KRN系)ハルミツ・北岡の大捜索!声まねショーコエまね(ひばりテレビ)THEうたごえ☆ファイト『声の職人頂上No.1決定戦』(つばめ放送)Lyra×Lyra(BSひばり)東京スカウトライブ(仮)(TOKYO QV)Pipp!!(KRN系)
記載項目
【チラシ表面】
公演名:第3回演奏会
団体名:みなぎブラスバンド若葉(わかば)
会場:羽村市市民交流会館 そよかぜ 大ホール
日時:2020年5月24日(日)
開場:13:30
開演:14:00
入場料:全席自由 500円
曲目:・ユニバリアード序曲と主題/カール・ベネディクト
・交響曲第4番 「ウィンドウズ・オブ・ミナモト」/マリカ・ボンテ
・委嘱作品/三宅 拓真
・POPS Selection
主催:みなぎブラスバンド若葉
後援:(現在未定)
お問い合わせ:みなぎブラスバンド若葉
wakaba.brass@kazemail.example
その他:会場へのアクセス方法や地図を入れて頂きたいと思います。
また、当団ロゴ、全体写真など使用していただければと思います。(添付ファイル)

【チラシ裏面】
ゲスト紹介については以来詳細をご確認ください。
当団紹介文については600文字程度で現在作成中です。
(チラシデザイン完成後、こちらで追記させていただきます。)
サイズ
A4
ページ数
両面
希望イメージ
シンプル 複雑
単色 カラフル
暗い 明るい
日常 高級
遊び心 厳粛
未来的 伝統的
女性的 男性的
希望する色
設定なし
納品ファイル
• イラストレーター形式 (.ai)
補足説明
交響曲第4番 「ウィンドウズ・オブ・ミナモト」
この曲は梅村雪舟や鳥居春泉の有名な版画6点をモチーフにした、歴史的な日本の木版画にインスピレーションをうけて作曲された6楽章からなる交響曲です。
1. 富士山 (雪舟-名峰四十八図)
2. 日本橋 (鳥居春泉-西国街道六十宿)
3. 相模灘荒波図 (雪舟-名峰四十八図)
4. 銀鶴山清月院 (鳥居春泉-清月院の風神門)
5. 原宿 月之霜 (鳥居春泉-西国街道六十宿)
6. 箱根 (鳥居春泉-西国街道六十宿)

```html
<!DOCTYPE html>
<html lang="ja">
<head>
<meta charset="utf-8">
<title>みなぎブラスバンド若葉 第3回演奏会</title>
<link href="https://fonts.googleapis.com/css2?family=Noto+Sans+JP:wght@400;500;700;900&family=Zen+Old+Mincho:wght@700;900&display=swap" rel="stylesheet">
<style>
  :root{
    --cream:#f6eed9;
    --paper:#fbf7ec;
    --ochre:#e8c25a;
    --ochre-deep:#c99a2e;
    --orange:#ef8a1d;
    --orange-deep:#e06a10;
    --ink:#2b2a28;
    --brown:#5b3f1d;
    --white:#ffffff;
  }
  *{margin:0;padding:0;box-sizing:border-box}
  html,body{width:849px;height:1200px;overflow:hidden;background:var(--cream)}
  body{font-family:"Noto Sans JP",sans-serif;color:var(--ink)}
  .flyer{position:relative;width:849px;height:1200px;overflow:hidden;background:var(--cream)}
  .hero-art{position:absolute;left:0;top:0;width:849px;height:770px;
    background:linear-gradient(170deg,#f3dc8c 0%,var(--ochre) 45%,#d9a94a 80%,#c58f35 100%)}
  .bands{position:absolute;left:0;top:0}
  .club{position:absolute;left:28px;top:26px;display:flex;align-items:center;gap:14px}
  .club-mark{width:70px;height:70px;border-radius:50%;background:var(--white);opacity:.9}
  .club-name{font-size:22px;font-weight:700;color:var(--white);letter-spacing:.04em}
  .program{position:absolute;left:170px;top:150px;font-size:15px;line-height:1.55;font-weight:500;color:var(--ink)}
  .program li{list-style:none}
  .program .sub{padding-left:1em}
  .edition{position:absolute;left:520px;top:20px;font-family:"Zen Old Mincho",serif;font-weight:900;color:var(--orange);font-size:70px;line-height:1}
  .edition .num{font-size:120px;color:var(--white);-webkit-text-stroke:0;margin:0 4px}
  .title{position:absolute;left:600px;top:160px;display:flex;flex-direction:column;font-family:"Zen Old Mincho",serif;font-weight:900;color:var(--white);font-size:150px;line-height:1}
  .date{position:absolute;left:36px;top:655px;color:var(--white);font-weight:900;font-size:62px;letter-spacing:.01em;line-height:1}
  .date .dow{font-size:44px}
  .times{position:absolute;left:40px;top:728px;color:var(--white);font-weight:700;font-size:20px}
  .times b{font-size:30px;font-weight:900;margin-right:16px}
  .venue{position:absolute;left:40px;top:790px;color:var(--orange-deep);font-weight:900;line-height:1.25}
  .venue .l1{font-size:32px}
  .venue .l2{font-size:36px}
  .venue .addr{font-size:13px;color:var(--ink);font-weight:500}
  .map{position:absolute;left:40px;top:895px;width:250px;height:205px;background:var(--white);display:flex;align-items:center;justify-content:center;font-size:26px;color:#c9c2b2;font-style:italic}
  .photo{position:absolute;left:330px;top:970px;width:490px;height:138px;background:linear-gradient(180deg,#9b8f86 0%,#5a4f48 60%,#3d3531 100%)}
  .info{position:absolute;left:40px;top:1128px;display:flex;align-items:center;gap:14px;font-size:14px;font-weight:700}
  .tag{background:var(--orange);color:var(--white);padding:2px 8px;font-size:12px}
  .info .org{color:var(--orange-deep);font-size:17px}
  .credits{position:absolute;left:0;top:1168px;width:849px;text-align:center;font-size:13px;font-weight:500}
</style>
</head>
<body>
<div class="flyer">
  <div class="hero-art" role="img" aria-label="東京の街並みと人々を描いた木版画風のイラスト"></div>
  <svg class="bands" width="849" height="1200" viewBox="0 0 849 1200" aria-hidden="true">
    <polygon points="0,640 849,470 849,560 0,780" fill="var(--orange)"/>
    <polygon points="0,780 849,560 849,600 0,820" fill="var(--ochre)" opacity=".85"/>
  </svg>

  <div class="club">
    <span class="club-mark"></span>
    <span class="club-name">みなぎブラスバンド若葉</span>
  </div>

  <ul class="program">
    <li>● ユニバリアード序曲と主題</li>
    <li class="sub">／カール・ベネディクト</li>
    <li>● 交響曲第4番</li>
    <li class="sub">「ウィンドウズ・オブ・ミナモト」</li>
    <li class="sub">／マリカ・ボンテ</li>
    <li>● 委嘱作品／三宅 拓真</li>
    <li>● POPS Selection</li>
  </ul>

  <div class="edition">第<span class="num">3</span>回</div>
  <h1 class="title"><span>演</span><span>奏</span><span>会</span></h1>

  <p class="date">2020.5.24<span class="dow">(日)</span></p>
  <p class="times">開場 <b>13:30</b> 開演 <b>14:00</b></p>

  <div class="venue">
    <p class="l1">羽村市市民交流会館</p>
    <p class="l2">そよかぜ 大ホール</p>
    <p class="addr">〒205-0099 東京都羽村市そよかぜ町3丁目2-8</p>
  </div>

  <div class="map" role="img" aria-label="会場へのアクセス地図">Map</div>
  <div class="photo" role="img" aria-label="みなぎブラスバンド若葉の全体写真"></div>

  <div class="info">
    <span class="tag">入場料</span><span>全席自由 500円</span>
    <span class="tag">お問い合わせ</span><span class="org">みなぎブラスバンド若葉</span>
    <span>wakaba.brass@kazemail.example</span>
  </div>
  <p class="credits">主催：みなぎブラスバンド若葉　後援：(現在未定)</p>
</div>
</body>
</html>
```